Electrical Contractors Business Card Design

I need a business card design for an electrical contracting business. A theme I was thinking of is the BE of Brightway Electrical both facing each other ie the second E is back to front and maybe each horizontal part of the E's are a different colours of the internal wires of TPS cable. The top would be blue(representing the sky), the middle green(representing the grass) and the lower would be brown(representing below the earth) (neutral,earth and active). And coming out of the back of each E going to each side of the business card would be the white outer sheath of TPS cable. I would like a big part of the card to be a very bright emerald flourescent green and maybe silver for the top half. the message I would like to send is that of an environmentally friendly, ethical business that delivers quality sevice on time.

Target Market(s)

40 to 80 year old home owners

Industry/Entity Type

Electrical

Contact Information for Business Card

Tom Keller
Brightway Electrical
EC 274381
Mob: 0417 592 064

```html
<!DOCTYPE html>
<html lang="en">
<head>
<meta charset="utf-8">
<title>Brightway Electrical – Business Card</title>
<link rel="stylesheet" href="https://fonts.googleapis.com/css2?family=Dosis:wght@400;500&display=swap">
<style>
  :root {
    --silver: #bfbfbf;
    --olive: #99a300;
    --lime: #cfdc12;
    --badge: #ffffff;
    --ink: #111111;
    --muted: #767676;
  }
  html, body {
    margin: 0;
    padding: 0;
    width: 1200px;
    height: 744px;
    overflow: hidden;
    background: #ffffff;
  }
  .business-card {
    position: relative;
    width: 1200px;
    height: 744px;
    overflow: hidden;
    font-family: "Dosis", sans-serif;
    background: var(--lime);
  }
  .backdrop-art {
    position: absolute;
    left: 0;
    top: 0;
    width: 1200px;
    height: 480px;
    background: linear-gradient(to bottom,
      var(--silver) 0%,
      var(--silver) 18%,
      var(--olive) 52%,
      var(--lime) 100%);
  }
  .brand {
    position: absolute;
    left: 600px;
    top: 250px;
    transform: translate(-50%, -50%);
    width: 400px;
    height: 400px;
    border-radius: 50%;
    background: var(--badge);
    display: flex;
    align-items: center;
    justify-content: center;
  }
  .brand-name {
    margin: 0;
    font-size: 170px;
    font-weight: 500;
    color: var(--ink);
    letter-spacing: 6px;
    line-height: 1;
  }
  .contact-name {
    position: absolute;
    left: 46px;
    top: 538px;
    margin: 0;
    font-size: 82px;
    font-weight: 400;
    color: var(--ink);
    line-height: 1;
  }
  .company-line {
    position: absolute;
    left: 30px;
    top: 648px;
    margin: 0;
    font-size: 40px;
    font-weight: 500;
    color: var(--muted);
    line-height: 1;
  }
  .phone {
    position: absolute;
    right: 22px;
    top: 610px;
    display: flex;
    align-items: center;
    gap: 8px;
    margin: 0;
    font-size: 58px;
    font-weight: 400;
    color: var(--ink);
    line-height: 1;
  }
  .phone-icon {
    width: 68px;
    height: 68px;
    display: block;
  }
</style>
</head>
<body>
  <main class="business-card">
    <div class="backdrop-art" role="img" aria-label="Decorative wave artwork in silver and green tones with a cable crossing the card"></div>

    <div class="brand">
      <p class="brand-name">BE</p>
    </div>

    <h1 class="contact-name">Tom Keller</h1>
    <p class="company-line">Brightway Electrical EC 274381</p>
    <p class="phone">
      <svg class="phone-icon" viewBox="0 0 72 72" aria-hidden="true">
        <circle cx="36" cy="36" r="31" fill="none" stroke="var(--ink)" stroke-width="5"/>
        <path d="M26,18 L32,18 L34,28 L29,31 C31,37 35,41 41,43 L44,38 L54,40 L54,46 C54,50 51,53 47,53 C33,52 20,39 19,25 C19,21 22,18 26,18 Z"
              fill="none" stroke="var(--ink)" stroke-width="4" stroke-linejoin="round"/>
      </svg>
      <span class="phone-number">0417 592 064</span>
    </p>
  </main>
</body>
</html>
```